Flash Banner Ads

I need the standard banner sizes : 728x90 , 160x600 , 300x250 .

We are needing banners for the site Glimmerbay.tv . The site is a video curation site of urban comedy/music/vlogs/skits that is updated with exclusive content by top vidquarry talents.

Taglines:
"The new curators of cool"
"The New Now"
"If you're not in BAY you're behind"
"Watch the latest urban video skits at Glimmerbay.tv"
"Watch Funny Videos"
"Like To Laugh watch new funny videos at Glimmerbay.tv"

Open to other tag lines around that area, the most important message to let the users know that we are a video site specializing in Urban.

I would really like these to be flash animated for more effect so whatever way you want to do that.

OR if you want some direction for flash animating, would love a banner similar to this: http://www.plakorio.com/blog/video-banners/ (if you see the banner at top how it is animated video banner then stops and has text)

Would love for this video part (https://www.vidquarry.com/watch?v=kR3TbW_QH27 02:49 to 02:53) to be animated in similar way and to say "The Verse Duel Spoof - Watch What Happens …. Only on Glimmerbay.tv " with our logo on it somewhere too.
Updates

Target Market(s)

Urban , Music , Hip hop , comedy , teens

Industry/Entity Type

Tv

Requirements
Must have
• Glimmerbay Logo and talking about Videos or something to that effect.
Nice to have
• Animated / Flash

```html
<!DOCTYPE html>
<html lang="en">
<head>
<meta charset="utf-8">
<title>Glimmerbay.tv Banner Set</title>
<link rel="stylesheet" href="https://fonts.googleapis.com/css2?family=Oswald:wght@500;700&family=Roboto:ital,wght@1,300&display=swap">
<style>
  :root {
    --page: #ffffff;
    --frame-dark: #1b1a1a;
    --frame-brown: #5b3e3f;
    --photo-deep: #2a1c1b;
    --photo-mid: #6b4a44;
    --crowd-tone: #7a5a55;
    --yellow: #f7ef6a;
    --yellow-deep: #e9c53a;
    --green: #8fe05a;
    --mint: #5fc496;
    --pink: #f3a0d8;
    --salmon: #f2b3a3;
    --orange: #f49a5c;
    --cyan: #7fe6f2;
    --ink: #1d1d1d;
    --navy: #2c3548;
    --gold-edge: #f3b53a;
    --white: #ffffff;
  }
  * { margin: 0; padding: 0; box-sizing: border-box; }
  html, body { width: 1200px; height: 960px; overflow: hidden; background: var(--page); }
  .canvas { position: relative; width: 1200px; height: 960px; }

  .banner {
    position: absolute; width: 360px; height: 299px;
    background: var(--frame-brown); overflow: hidden;
    font-family: "Oswald", "Arial Narrow", sans-serif;
  }
  .banner::after {
    content: ""; position: absolute; top: 0; right: 0; width: 22px; height: 100%;
    background: var(--frame-dark);
  }
  .banner::before {
    content: ""; position: absolute; top: 0; left: 0; width: 8px; height: 100%;
    background: var(--frame-dark); z-index: 1;
  }
  .banner--curators { left: 220px; top: 136px; }
  .banner--spoof { left: 661px; top: 136px; }
  .banner--spoof-final { left: 661px; top: 503px; }

  .crowd-photo {
    position: absolute; left: 24px; top: 40px; width: 316px; height: 236px;
    background: linear-gradient(180deg, var(--crowd-tone), var(--frame-brown));
    opacity: .85;
  }
  .host-photo {
    position: absolute; left: 40px; top: 84px; width: 300px; height: 215px;
    background: radial-gradient(ellipse at 50% 35%, var(--photo-mid) 0%, var(--photo-deep) 75%);
    border-radius: 40% 40% 0 0 / 30% 30% 0 0;
  }

  .brand-mark {
    position: absolute; left: 12px; top: 80px; z-index: 3;
    display: flex; align-items: center; gap: 4px;
  }
  .brand-mark__dot { width: 56px; height: 56px; border-radius: 50%; background: var(--yellow); }
  .brand-mark__name { font-weight: 700; font-size: 15px; color: var(--yellow); letter-spacing: .3px; }

  .headline {
    position: absolute; left: 0; right: 14px; top: 6px; text-align: center; z-index: 3;
    font-weight: 700; font-size: 31px; line-height: 1.1; letter-spacing: -.3px;
  }
  .headline .w1 { color: var(--yellow); }
  .headline .w2 { color: var(--green); }
  .headline .w3 { color: var(--salmon); }
  .headline .w4 { color: var(--orange); }
  .headline .w5 { color: var(--yellow-deep); }
  .subline {
    position: absolute; left: 0; right: 14px; top: 44px; text-align: center; z-index: 3;
    font-family: "Roboto", sans-serif; font-style: italic; font-weight: 300;
    font-size: 23px; color: var(--cyan);
  }

  .title-strip {
    position: absolute; left: 22px; top: 6px; width: 312px; height: 40px; z-index: 3;
  }
  .title-strip svg { position: absolute; inset: 0; }
  .title-strip__text {
    position: absolute; inset: 0; display: flex; align-items: center; justify-content: center;
    font-weight: 700; font-size: 25px; color: var(--ink); letter-spacing: -.2px;
  }

  .tag {
    position: absolute; z-index: 3; height: 30px; display: flex; align-items: center; justify-content: center;
    font-weight: 700; font-size: 21px; color: var(--ink); line-height: 1;
  }
  .tag--yellow { background: var(--yellow); }
  .tag--mint { background: var(--mint); }
  .tag--pink { background: var(--pink); }
  .tag--orange { background: var(--orange); font-size: 18px; }

  .banner--spoof .tag--watch { left: 54px; top: 248px; width: 66px; }
  .banner--spoof .tag--what { left: 125px; top: 240px; width: 60px; }
  .banner--spoof .tag--happens { left: 190px; top: 250px; width: 92px; }
  .banner--spoof .tag--dots { left: 286px; top: 262px; width: 24px; height: 18px; }

  .banner--spoof-final .tag--watch { left: 2px; top: 222px; width: 70px; transform: rotate(32deg); }
  .banner--spoof-final .tag--what { left: 64px; top: 206px; width: 60px; transform: rotate(-22deg); }
  .banner--spoof-final .tag--happens { left: 97px; top: 257px; width: 92px; }
  .banner--spoof-final .tag--dots { left: 190px; top: 262px; width: 20px; height: 26px; transform: rotate(-12deg); }

  .only-on {
    position: absolute; left: 215px; top: 211px; width: 130px; height: 74px; z-index: 3;
    background: var(--navy); border: 4px solid var(--gold-edge); border-radius: 12px;
    transform: rotate(-3deg);
    display: flex; flex-direction: column; align-items: center; justify-content: center;
    color: var(--white); font-family: "Roboto", sans-serif;
  }
  .only-on__lead { font-size: 15px; font-style: normal; }
  .only-on__site { font-family: "Oswald", sans-serif; font-weight: 500; font-size: 22px; }
</style>
</head>
<body>
<main class="canvas">

  <section class="banner banner--curators">
    <div class="host-photo" role="img" aria-label="Young man in a snapback cap holding the brim with both hands"></div>
    <div class="headline"><span class="w1">The</span> <span class="w2">new</span> <span class="w3">curators</span> <span class="w4">of</span> <span class="w5">cool</span></div>
    <div class="subline">Watch Funny Videos</div>
    <div class="brand-mark"><span class="brand-mark__dot"></span><span class="brand-mark__name">Glimmerbay</span></div>
  </section>

  <section class="banner banner--spoof">
    <div class="crowd-photo" role="img" aria-label="Crowd gathered around a street verse duel"></div>
    <div class="host-photo" role="img" aria-label="Young man in a snapback cap holding the brim with both hands"></div>
    <div class="title-strip">
      <svg viewBox="0 0 312 40" preserveAspectRatio="none" aria-hidden="true">
        <defs><linearGradient id="stripA" x1="0" y1="0" x2="0" y2="1"><stop offset="0" stop-color="#f7ef6a"/><stop offset="1" stop-color="#e0b932"/></linearGradient></defs>
        <path d="M4 4 L60 1 L120 5 L190 2 L250 5 L308 2 L305 14 L311 24 L306 38 L240 35 L170 39 L100 35 L40 39 L2 36 L6 22 L1 12 Z" fill="url(#stripA)"/>
      </svg>
      <div class="title-strip__text">The Verse Duel Spoof</div>
    </div>
    <div class="brand-mark"><span class="brand-mark__dot"></span><span class="brand-mark__name">Glimmerbay</span></div>
    <div class="tag tag--yellow tag--watch">Watch</div>
    <div class="tag tag--mint tag--what">What</div>
    <div class="tag tag--pink tag--happens">Happens</div>
    <div class="tag tag--orange tag--dots">...</div>
  </section>

  <section class="banner banner--spoof-final">
    <div class="crowd-photo" role="img" aria-label="Crowd gathered around a street verse duel"></div>
    <div class="host-photo" role="img" aria-label="Young man in a snapback cap holding the brim with both hands"></div>
    <div class="title-strip">
      <svg viewBox="0 0 312 40" preserveAspectRatio="none" aria-hidden="true">
        <defs><linearGradient id="stripB" x1="0" y1="0" x2="0" y2="1"><stop offset="0" stop-color="#f7ef6a"/><stop offset="1" stop-color="#e0b932"/></linearGradient></defs>
        <path d="M4 4 L60 1 L120 5 L190 2 L250 5 L308 2 L305 14 L311 24 L306 38 L240 35 L170 39 L100 35 L40 39 L2 36 L6 22 L1 12 Z" fill="url(#stripB)"/>
      </svg>
      <div class="title-strip__text">The Verse Duel Spoof</div>
    </div>
    <div class="brand-mark"><span class="brand-mark__dot"></span><span class="brand-mark__name">Glimmerbay</span></div>
    <div class="tag tag--yellow tag--watch">Watch</div>
    <div class="tag tag--mint tag--what">What</div>
    <div class="tag tag--pink tag--happens">Happens</div>
    <div class="tag tag--orange tag--dots">:</div>
    <div class="only-on">
      <span class="only-on__lead">Only on</span>
      <span class="only-on__site">Glimmerbay.tv</span>
    </div>
  </section>

</main>
</body>
</html>
```